Professional Services - letterhead / business cards

The company (veltaro holdings) will provide services to Investment Funds and large investors in Spain. I have recently chosen a logo that I am attaching.

I would like a simple stationary design that i could use as letter head, business cards and "with compliments" cards.

I am not quite sure which color I will mostly use for the logo, in the email signature I will probably lean towards the white background and grey letters. I am attaching my favourite options.

Target Market(s)

Large Multinationals, Investment funds and Law firms

Industry/Entity Type

Business

Requirements
Must have
• my details are:
Luis R. Andrade
Veltaro Holdings S.L.
Casa de Valdehondo
Calle del Olmo Tardío 42
28017 Madrid
T: +34 (91) 807-3356
M: +34 (655) 718-904
e-mail: landrade@veltaroholdings.example

```html
<!DOCTYPE html>
<html lang="es">
<head>
<meta charset="utf-8">
<title>Veltaro Holdings – Business Card</title>
<link rel="stylesheet" href="https://fonts.googleapis.com/css2?family=Jost:wght@300;400;600&display=swap">
<style>
  :root {
    --navy: #27286b;
    --band-grey: #a7a9ab;
    --card-white: #ffffff;
    --backdrop: #e9e7e4;
    --text-dark: #2b2b33;
    --rule-grey: #bfc0c2;
  }
  * { box-sizing: border-box; margin: 0; padding: 0; }
  html, body { width: 1200px; height: 719px; overflow: hidden; }
  body {
    background: var(--backdrop);
    font-family: "Jost", sans-serif;
    position: relative;
  }
  .card {
    position: absolute;
    top: 194px;
    width: 520px;
    height: 330px;
    border-radius: 20px;
    background: var(--card-white);
    overflow: hidden;
    box-shadow: 0 6px 18px rgba(0,0,0,0.18);
  }
  .card--front { left: 50px; }
  .card--back { left: 630px; }

  .wordmark {
    position: absolute;
    font-weight: 300;
    color: var(--navy);
    font-size: 44px;
    letter-spacing: 0.5px;
    white-space: nowrap;
  }
  .card--front .wordmark { left: 62px; top: 58px; }
  .card--back .wordmark { left: 0; right: 0; top: 96px; text-align: center; }

  .contact-band {
    position: absolute;
    left: 0; right: 0;
    top: 168px;
    height: 104px;
    background: var(--band-grey);
  }
  .address {
    position: absolute;
    right: 290px;
    top: 24px;
    text-align: right;
    font-size: 14px;
    line-height: 19px;
    color: var(--text-dark);
  }
  .band-rule {
    position: absolute;
    left: 244px;
    top: 16px;
    width: 1px;
    height: 72px;
    background: #6f7174;
  }
  .contact-list {
    position: absolute;
    left: 258px;
    top: 16px;
    list-style: none;
    font-size: 14px;
    line-height: 24px;
    color: var(--text-dark);
  }
  .contact-list li { display: flex; align-items: center; gap: 8px; }
  .contact-list svg { width: 12px; height: 12px; flex: none; }

  .name-band {
    position: absolute;
    left: 0; right: 0; bottom: 0;
    height: 58px;
    background: var(--navy);
    color: var(--card-white);
    display: flex;
    align-items: center;
    padding-left: 96px;
  }
  .person-name { font-weight: 600; font-size: 20px; letter-spacing: 0.6px; }
  .company-name { font-size: 14px; margin-left: 8px; font-weight: 400; }

  .web-address {
    position: absolute;
    left: 0; right: 0;
    top: 232px;
    text-align: center;
    font-size: 14px;
    font-weight: 600;
    letter-spacing: 7px;
    color: var(--text-dark);
  }
</style>
</head>
<body>

  <section class="card card--front" aria-label="Business card, front">
    <div class="wordmark">veltaro holdings</div>

    <div class="contact-band">
      <p class="address">Casa de Valdehondo<br>Calle del Olmo Tardío 42<br>28017 Madrid</p>
      <div class="band-rule"></div>
      <ul class="contact-list">
        <li>
          <svg viewBox="0 0 12 12" aria-hidden="true"><path d="M2.5 1h2l1 2.6-1.3 1a6 6 0 0 0 3.2 3.2l1-1.3 2.6 1v2A1 1 0 0 1 10 11 9 9 0 0 1 1 2a1 1 0 0 1 1.5-1z" fill="var(--text-dark)"/></svg>
          +34 (91) 807-3356
        </li>
        <li>
          <svg viewBox="0 0 12 12" aria-hidden="true"><rect x="3" y="0.5" width="6" height="11" rx="1" fill="none" stroke="var(--text-dark)"/><rect x="4.2" y="2" width="3.6" height="5.5" fill="var(--text-dark)"/></svg>
          +34 (655) 718-904
        </li>
        <li>
          <svg viewBox="0 0 12 12" aria-hidden="true"><rect x="0.5" y="2.5" width="11" height="7.5" rx="1" fill="var(--text-dark)"/><path d="M1 3l5 3.8L11 3" fill="none" stroke="var(--band-grey)"/></svg>
          landrade@veltaroholdings.example
        </li>
      </ul>
    </div>

    <div class="name-band">
      <span class="person-name">Luis R. Andrade,</span>
      <span class="company-name">Veltaro Holdings S.L.</span>
    </div>
  </section>

  <section class="card card--back" aria-label="Business card, back">
    <div class="wordmark">veltaro holdings</div>
    <p class="web-address">www.veltaro.example</p>
  </section>

</body>
</html>
```